Harbor Dental, LLC business card project

Business card to be designed with current logo.
Dental office- please keep design of card that looks clean and professional.
Please include the following info:
Harbor Dental, LLC
Dr. Corinne Pelham
3187 Elmwood
Bethlehem, PA 18015
610-392-7158
harbordental.office@quillmail.net
Updates
Hello everyone-
Project Deadline Extended
Reason: Just got back from overseas- will look at all designs and provide feedback. Thank you!
Project Deadline Extended
Reason: Polling my friends for the final selection-
thank you to all those that participated- so many talented designers!
Business

```html
<!DOCTYPE html>
<html lang="en">
<head>
<meta charset="utf-8">
<title>Harbor Dental, LLC – Business Card</title>
<link rel="stylesheet" href="https://fonts.googleapis.com/css2?family=Carlito:wght@400;700&display=swap">
<style>
  :root {
    --backdrop: #a8a8a8;
    --brand-green: #64a140;
    --accent-lime: #a6c93a;
    --icon-green: #8bbf3a;
    --card-white: #ffffff;
    --ink: #2b2b2b;
    --ink-strong: #1f1f1f;
  }
  * { margin: 0; padding: 0; box-sizing: border-box; }
  html, body {
    width: 1200px;
    height: 960px;
    overflow: hidden;
  }
  body {
    position: relative;
    background: var(--backdrop);
    font-family: "Carlito", "Calibri", sans-serif;
  }
  .card {
    position: absolute;
    left: 320px;
    width: 575px;
  }
  .card--front {
    top: 97px;
    height: 379px;
    background: var(--brand-green);
  }
  .card--back {
    top: 506px;
    height: 376px;
    background: var(--card-white);
  }
  .wordmark {
    position: absolute;
    display: flex;
    align-items: center;
    gap: 10px;
    font-weight: 400;
    white-space: nowrap;
  }
  .wordmark__dot {
    width: 18px;
    height: 18px;
    border-radius: 50%;
    flex: none;
  }
  .card--front .wordmark {
    left: 148px;
    top: 160px;
    font-size: 34px;
    color: var(--card-white);
  }
  .card--front .wordmark__dot { background: var(--card-white); }
  .card--back .wordmark {
    left: 28px;
    top: 44px;
    font-size: 38px;
    color: var(--brand-green);
  }
  .card--back .wordmark__dot { background: var(--brand-green); }
  .contact {
    position: absolute;
    left: 56px;
    top: 207px;
    color: var(--ink);
    font-size: 15.5px;
    line-height: 19px;
  }
  .contact__company {
    font-weight: 700;
    font-size: 17.5px;
    color: var(--ink-strong);
    margin-bottom: 4px;
  }
  .contact__row {
    display: flex;
    align-items: center;
    gap: 7px;
  }
  .contact__row--indent { padding-left: 21px; }
  .contact__icon {
    width: 14px;
    height: 14px;
    flex: none;
    fill: var(--icon-green);
  }
  .holder-name {
    position: absolute;
    right: 36px;
    top: 204px;
    font-weight: 700;
    font-size: 22px;
    color: var(--ink-strong);
  }
  .footer-band {
    position: absolute;
    left: 0;
    bottom: 0;
    width: 518px;
    height: 32px;
    background: var(--brand-green);
  }
  .footer-accent {
    position: absolute;
    right: 0;
    bottom: 0;
    width: 51px;
    height: 32px;
    background: var(--accent-lime);
  }
</style>
</head>
<body>

  <section class="card card--front" aria-label="Business card front">
    <div class="wordmark">
      <span class="wordmark__dot"></span>
      <span class="wordmark__name">Harbor Dental, LLC</span>
    </div>
  </section>

  <section class="card card--back" aria-label="Business card back">
    <div class="wordmark">
      <span class="wordmark__dot"></span>
      <span class="wordmark__name">Harbor Dental, LLC</span>
    </div>

    <div class="contact">
      <p class="contact__company">Harbor Dental, LLC</p>
      <p class="contact__row">
        <svg class="contact__icon" viewBox="0 0 14 14" aria-hidden="true">
          <path d="M7 1 L13 6.5 H11 V13 H8.3 V9 H5.7 V13 H3 V6.5 H1 Z"/>
        </svg>
        <span>3187 Elmwood</span>
      </p>
      <p class="contact__row contact__row--indent">Bethlehem, PA 18015</p>
      <p class="contact__row">
        <svg class="contact__icon" viewBox="0 0 14 14" aria-hidden="true">
          <path d="M3.2 1.2 L5.4 3.6 L4.3 5.2 C5 7 6.9 8.9 8.8 9.7 L10.4 8.6 L12.8 10.8 L11.4 12.6 C6.8 12.4 1.6 7.2 1.4 2.6 Z"/>
        </svg>
        <span>610-392-7158</span>
      </p>
      <p class="contact__row">
        <svg class="contact__icon" viewBox="0 0 14 14" aria-hidden="true">
          <path d="M1 3 H13 V11 H1 Z M1.8 3.6 L7 7.6 L12.2 3.6" stroke="#ffffff" stroke-width="0.9"/>
        </svg>
        <span>harbordental.office@quillmail.net</span>
      </p>
    </div>

    <p class="holder-name">Dr. Corinne Pelham</p>

    <div class="footer-band"></div>
    <div class="footer-accent"></div>
  </section>

</body>
</html>
```